Letterhead Design for Law Firm that Specializes in Property Damage Litigation

We are looking for a redesign of our letterhead. Our current letterhead lists all of our current staff members and we'd like to come up with a design that does NOT list all of the staff members so that it does not need to be updated with every newly hired employee. Must be in editable format.

We are a law firm that specializes in property damage, so we need something that is professional, yet modern. The final design should use our existing logo and should use a blue color scheme (alternate colors would be gray, black, and white).

Industry/Entity Type

Legal

Colors
0054AA
0677BA
7BADD7
CADEEF
E8F1F8

```html
<!DOCTYPE html>
<html lang="en">
<head>
<meta charset="utf-8">
<title>Harrow Lindqvist &amp; Penrose — Letterhead</title>
<link href="https://fonts.googleapis.com/css2?family=Cinzel:wght@500&family=PT+Sans+Narrow:wght@400;700&family=Tinos&family=Montserrat:wght@500&display=swap" rel="stylesheet">
<style>
:root{
  --navy:#17305f;
  --grey-dark:#606060;
  --grey-mid:#808080;
  --text-grey:#3a3a3a;
  --ink:#1a1a1a;
  --backdrop:#e8e8e8;
  --white:#ffffff;
}
*{margin:0;padding:0;box-sizing:border-box}
html,body{width:1200px;height:1200px;overflow:hidden;background:var(--backdrop)}
.letterhead{position:absolute;left:233px;top:125px;width:734px;height:950px;background:var(--white);border:2px solid var(--grey-mid);overflow:hidden}
.decor{position:absolute;left:0;top:0;width:730px;height:946px}
.office{position:absolute;top:39px;width:170px}
.office--pa{left:0}
.office--nj{left:560px}
.office__label{border:1px solid var(--grey-mid);height:16px;font-family:'Cinzel',serif;font-size:10.5px;color:var(--text-grey);letter-spacing:.3px;line-height:14px}
.office--pa .office__label{border-left:none;padding-left:32px}
.office--nj .office__label{border-right:none;padding-left:10px}
.office__list{list-style:none;margin-top:7px;font-family:'PT Sans Narrow',sans-serif;font-size:9.8px;color:var(--text-grey)}
.office--pa .office__list{padding-left:32px}
.office--nj .office__list{padding-left:10px}
.office__list li{height:17px;display:flex;align-items:center;gap:5px}
.office__list li.indent{padding-left:13px}
.office__list svg{width:8px;height:8px;flex:none}
.firm{position:absolute;left:200px;top:52px;width:330px;text-align:center}
.firm__name{font-family:'PT Sans Narrow',sans-serif;font-weight:700;font-size:27px;line-height:30px;color:var(--navy)}
.firm__tagline{margin-top:14px;font-family:'Montserrat',sans-serif;font-weight:500;font-size:10px;letter-spacing:2.6px;color:var(--grey-dark)}
.body-copy{position:absolute;left:67px;top:259px;width:596px;font-family:'Tinos',serif;font-size:14.5px;line-height:20.7px;color:var(--ink)}
.body-copy p{margin-bottom:27px}
</style>
</head>
<body>
<div class="letterhead">
  <svg class="decor" viewBox="0 0 730 946" preserveAspectRatio="none" aria-hidden="true">
    <defs>
      <linearGradient id="headerFade" x1="0" y1="0" x2="0" y2="1">
        <stop offset="0" stop-color="#c6c6c6"/>
        <stop offset="1" stop-color="#ffffff"/>
      </linearGradient>
      <linearGradient id="swoosh" x1="0" y1="0" x2="1" y2="0">
        <stop offset="0" stop-color="#f2f2f2"/>
        <stop offset=".6" stop-color="#c4c4c4"/>
        <stop offset="1" stop-color="#dcdcdc"/>
      </linearGradient>
    </defs>
    <rect x="0" y="0" width="730" height="230" fill="url(#headerFade)"/>
    <path d="M0 164 C120 186 200 196 320 178 C430 160 520 136 730 182 L730 230 L0 230 Z" fill="url(#swoosh)"/>
    <path d="M0 196 C80 214 160 222 260 210 C360 198 440 170 520 160 C600 150 680 170 730 184 L730 240 L0 240 Z" fill="#ffffff"/>
    <path d="M0 810 C100 832 180 840 280 834 C400 826 480 790 574 788 C640 786 700 810 730 822 L730 946 L0 946 Z" fill="var(--grey-dark)"/>
    <path d="M0 838 C80 856 160 864 250 858 C370 850 460 800 570 796 C640 794 700 812 730 822 L730 946 L0 946 Z" fill="var(--navy)"/>
  </svg>

  <section class="office office--pa">
    <div class="office__label">PHILADELPHIA OFFICE</div>
    <ul class="office__list">
      <li><svg viewBox="0 0 10 10"><circle cx="5" cy="5" r="5" fill="#333"/><path d="M3 2.5l1 1-.6.8c.4.9 1 1.5 1.9 1.9l.8-.6 1 1-.7.9C4.8 7.3 2.7 5.2 2.5 3.2z" fill="#fff"/></svg>215.555.0140</li>
      <li><svg viewBox="0 0 10 10"><circle cx="5" cy="5" r="5" fill="#333"/><rect x="3" y="3" width="4" height="4" fill="#fff"/><rect x="3.8" y="3.8" width="2.4" height="1" fill="#333"/></svg>215.555.0177</li>
      <li><svg viewBox="0 0 10 10"><circle cx="5" cy="5" r="5" fill="#333"/><path d="M5 2.2a1.9 1.9 0 0 1 1.9 1.9C6.9 5.5 5 7.8 5 7.8S3.1 5.5 3.1 4.1A1.9 1.9 0 0 1 5 2.2z" fill="#fff"/><circle cx="5" cy="4.1" r=".7" fill="#333"/></svg>2200 Market Street Suite 840</li>
      <li class="indent">Philadelphia, PA 19103</li>
    </ul>
  </section>

  <header class="firm">
    <div class="firm__name">Harrow Lindqvist &amp; Penrose</div>
    <div class="firm__tagline">THE PROPERTY DAMAGE ATTORNEYS</div>
  </header>

  <section class="office office--nj">
    <div class="office__label">NEW JERSEY OFFICE</div>
    <ul class="office__list">
      <li><svg viewBox="0 0 10 10"><circle cx="5" cy="5" r="5" fill="#333"/><path d="M3 2.5l1 1-.6.8c.4.9 1 1.5 1.9 1.9l.8-.6 1 1-.7.9C4.8 7.3 2.7 5.2 2.5 3.2z" fill="#fff"/></svg>856. 555. 0162</li>
      <li><svg viewBox="0 0 10 10"><circle cx="5" cy="5" r="5" fill="#333"/><rect x="3" y="3" width="4" height="4" fill="#fff"/><rect x="3.8" y="3.8" width="2.4" height="1" fill="#333"/></svg>215.555.0177</li>
      <li><svg viewBox="0 0 10 10"><circle cx="5" cy="5" r="5" fill="#333"/><path d="M5 2.2a1.9 1.9 0 0 1 1.9 1.9C6.9 5.5 5 7.8 5 7.8S3.1 5.5 3.1 4.1A1.9 1.9 0 0 1 5 2.2z" fill="#fff"/><circle cx="5" cy="4.1" r=".7" fill="#333"/></svg>415 Haddon Avenue Suite 310</li>
      <li class="indent">Cherry Hill, NJ. 08002</li>
    </ul>
  </section>

  <main class="body-copy">
    <p>Lorem ipsum dolor sit amet, consectetur adipiscing elit. Vestibulum erat velit, dapibus non dolor sit amet, vestibulum pharetra dolor. Vestibulum interdum augue quis leo mollis convallis. Nullam vestibulum faucibus dui ut hendrerit. Mauris at molestie nisl. Aenean ultricies suscipit sem, sit amet convallis lorem efficitur sit amet. Phasellus ut lectus pharetra, ullamcorper ligula eget, rutrum lectus. Nam mattis, libero quis fringilla sollicitudin, ex turpis scelerisque eros, ut elementum arcu urna tristique augue. Orci varius natoque penatibus et magnis dis parturient montes, nascetur ridiculus mus. Nulla a nisl et ante rutrum vehicula. Nulla dapibus ut ligula in dignissim. Vivamus ornare sollicitudin ligula malesuada pellentesque. Praesent accumsan ipsum id orci facilisis, at luctus nibh finibus.</p>
    <p>Nunc malesuada cursus nulla, ut congue massa elementum id. Curabitur quis lobortis eros, et volutpat tortor. Sed tincidunt massa vitae turpis mollis, nec consectetur metus lobortis. Etiam at dictum tellus. Suspendisse sed justo ut turpis varius lacinia sed eget mauris. Donec gravida ante vel neque hendrerit venenatis. Mauris arcu felis, ornare tempor ex eget, venenatis cursus erat. Class aptent taciti sociosqu ad litora torquent per conubia nostra, per inceptos himenaeos. Cras malesuada arcu sed tincidunt feugiat. Aenean ut lorem ut eros placerat varius sit amet vitae magna. Vestibulum aliquet odio non massa semper, a imperdiet ex ultrices. In vel dui et turpis vulputate commodo ut in leo.</p>
    <p>Donec ut ligula varius turpis bibendum finibus. Donec vel pulvinar turpis. Donec volutpat est eu lectus elementum tempor. Maecenas ut nisl in massa dignissim commodo. Sed vitae ipsum nibh. Pellentesque lacinia eros quis urna maximus aliquam. Phasellus iaculis ipsum nulla, sed sollicitudin urna ultricies non. Vestibulum dapibus arcu elit, et placerat orci ullamcorper quis. Nulla pharetra ex quis pharetra ultrices. Vivamus luctus sapien quis dolor ullamcorper egestas.</p>
  </main>
</div>
</body>
</html>
```